Redesign, cleanup and edit my Presentations

I have a series of power points that I use for training purposes. They were made by me over time. During the last couple years, I have evolved their look and content over time, but not consistently. More specifically, I have not gone back to re-edit the older decks. So, some decks are too wordy, too long, or and don't look consistent.

I am looking someone who can create a good design that I can use going forward, and who could also apply that theme to the existing decks, along with editing the existing, and future decks, too.

I have a lot of slides to produce and/or edit -approximately 500. But this request is a test to find a powerpoint partner. I am supplying 2 decks. One that's older and more wordy than the other. I would like to see what you would suggest we do differently. So that's what you are bidding on today. Also, you do not have to complete deck "Phase 7.4." I only need enough of the deck done to see where you would take it. Maybe 10 slides? Your choice. However, with that deck, there are lots of opportunities to clarify, re-align, and minimize within that deck.

But, if you are selected, I want to engage with you on an ongoing basis, and send more material your way. Then, you will be engaged to complete all decks.

Please ask me any questions to help you gain a better understanding of this project.

Target Market(s)

People in management, technical, medical, and financial fields who wish to become independent consultants.

Industry/Entity Type

Business Consultant

Font styles to use
Sans Serif

Requirements
Must have
• Use the existing color theme:
• yellow/gold - #f5b300,
• blue - 2b74a6
• Logo doesn't change
• Preferred fonts: Raleway for headings and Open Sans for general text
• Any pictures and graphics should have no copyright restrictions. That is, I should have use of the work without charge.
Nice to have
• I prefer a flat graphic style, although you can use pictures where it conveys a point more effectively.
• Ability to convert the presentations to Google Slides and Apple's Keynote apps.
• Ability to convert presentation to video
Should not have
• Restricted use graphics, photos, or other content.

```html
<!DOCTYPE html>
<html lang="en">
<head>
<meta charset="UTF-8">
<title>B2C Characteristics</title>
<link href="https://fonts.googleapis.com/css2?family=Arimo:wght@700&family=Source+Sans+3:wght@400;700&display=swap" rel="stylesheet">
<style>
  :root {
    --brand-blue: #1f77a5;
    --brand-gold: #f8b11b;
    --paper: #ffffff;
  }
  * { margin: 0; padding: 0; box-sizing: border-box; }
  html, body {
    width: 1200px;
    height: 630px;
    overflow: hidden;
    background: var(--paper);
  }
  .slide {
    position: relative;
    width: 1200px;
    height: 630px;
    background: var(--paper);
    overflow: hidden;
  }
  .slide-title {
    position: absolute;
    top: 0;
    left: 0;
    width: 100%;
    text-align: center;
    font-family: "Arimo", Arial, sans-serif;
    font-weight: 700;
    font-size: 63px;
    line-height: 63px;
    letter-spacing: 1px;
    color: var(--brand-blue);
    padding-top: 4px;
  }
  .trait-icon {
    position: absolute;
    left: 50%;
    transform: translateX(-50%);
    fill: var(--brand-gold);
  }
  .icon-individual { top: 80px; width: 82px; height: 82px; }
  .icon-emotive { top: 227px; width: 70px; height: 60px; }
  .icon-perception { top: 351px; width: 122px; height: 60px; }
  .icon-impulse { top: 466px; width: 80px; height: 78px; }
  .trait-text {
    position: absolute;
    left: 0;
    width: 100%;
    text-align: center;
    font-family: "Source Sans 3", "Open Sans", sans-serif;
    font-weight: 400;
    font-size: 27px;
    line-height: 32px;
    color: var(--brand-blue);
  }
  .text-individual { top: 165px; }
  .text-emotive { top: 291px; }
  .text-perception { top: 417px; }
  .text-impulse { top: 543px; }
  .brand-mark {
    position: absolute;
    left: 952px;
    top: 548px;
    display: flex;
    align-items: center;
    gap: 10px;
  }
  .brand-dot {
    width: 44px;
    height: 44px;
    border-radius: 50%;
    background: var(--brand-gold);
  }
  .brand-name {
    font-family: "Source Sans 3", "Open Sans", sans-serif;
    font-weight: 700;
    font-size: 46px;
    line-height: 46px;
    color: var(--brand-blue);
  }
  .footer-band {
    position: absolute;
    left: 0;
    bottom: 0;
    width: 100%;
    height: 20px;
    background: var(--brand-blue);
  }
</style>
</head>
<body>
<main class="slide">
  <h1 class="slide-title">B2C CHARACTERISTICS</h1>

  <svg class="trait-icon icon-individual" viewBox="0 0 100 100" aria-hidden="true">
    <g fill="none" stroke="var(--brand-gold)" stroke-width="9">
      <path d="M16 36 A38 38 0 0 1 88 42"/>
      <path d="M84 64 A38 38 0 0 1 12 58"/>
    </g>
    <polygon points="2,40 28,22 26,48"/>
    <polygon points="98,58 72,78 74,50"/>
    <circle cx="50" cy="38" r="13"/>
    <path d="M27 74 Q28 52 50 52 Q72 52 73 74 Z"/>
  </svg>
  <p class="trait-text text-individual">Purchases are typically based on an individual decision</p>

  <svg class="trait-icon icon-emotive" viewBox="0 0 116 98" aria-hidden="true">
    <path d="M58 98 L8 48 A28 28 0 0 1 58 14 A28 28 0 0 1 108 48 Z"/>
  </svg>
  <p class="trait-text text-emotive">Purchases are more emotive, and less logical</p>

  <svg class="trait-icon icon-perception" viewBox="0 0 200 98" aria-hidden="true">
    <path d="M0 49 Q100 -46 200 49 Q100 144 0 49 Z"/>
    <circle cx="100" cy="49" r="42" fill="var(--paper)"/>
    <circle cx="100" cy="49" r="34"/>
    <circle cx="76" cy="32" r="10" fill="var(--paper)"/>
    <circle cx="100" cy="50" r="14" fill="var(--paper)"/>
    <circle cx="76" cy="32" r="9"/>
    <circle cx="100" cy="50" r="13"/>
  </svg>
  <p class="trait-text text-perception">Make purchases based on their own perceptions, wants and needs</p>

  <svg class="trait-icon icon-impulse" viewBox="0 0 130 126" aria-hidden="true">
    <path d="M70 0 C108 0 130 24 128 60 C126 78 112 90 92 106 L92 124 L28 124 L26 100 L2 96 L24 62 C24 22 42 0 70 0 Z"/>
    <g fill="var(--paper)">
      <circle cx="62" cy="22" r="8"/>
      <circle cx="78" cy="18" r="9"/>
      <circle cx="94" cy="24" r="8"/>
      <circle cx="106" cy="34" r="7"/>
      <circle cx="112" cy="46" r="6"/>
      <circle cx="52" cy="30" r="6"/>
    </g>
    <polyline points="46,36 70,36 76,26 84,46 90,34 114,38" fill="none" stroke="var(--brand-gold)" stroke-width="3"/>
  </svg>
  <p class="trait-text text-impulse">Purchases can be impulsive</p>

  <div class="brand-mark">
    <span class="brand-dot"></span>
    <span class="brand-name">Veltrana</span>
  </div>

  <div class="footer-band"></div>
</main>
</body>
</html>
```